A simple Chatterbook Ad (not Chatterbook Page) for weight loss surgery

It’s a simple ad in terms of the text.

The text should say:
Curious about weight loss surgery?
This 30 second quiz will tell you which procedure will suit you best

I'm open to variations in the text if it is thought to enhance the ad.

Targeted towards obese individuals who have been unable to lose weight with diet and exercise. My industry is weight loss surgery – webpage www.marcusbellweather.com.au. Clicking the ad leads to a quiz on my webpage relating to weight loss surgery. Most frequent users of this service are females (75%) between ages of 35 and 55 years.

Successful weight loss surgery can enable individuals who have been unable to lose weight to lose a substantial amount of the excess weight they are carrying to be healthier and happier.

```html
<!DOCTYPE html>
<html lang="en">
<head>
<meta charset="utf-8">
<title>Marcus Bellweather – Weight Loss Surgery Quiz Ad</title>
<link href="https://fonts.googleapis.com/css2?family=Playfair+Display:wght@400&family=Jost:wght@300;400&display=swap" rel="stylesheet">
<style>
  :root {
    --panel-top: rgba(28, 128, 128, 0.88);
    --panel-bottom: rgba(62, 180, 170, 0.95);
    --white: #ffffff;
    --button: #000000;
    --photo-light: #cfd0d8;
    --photo-mid: #8d90b8;
    --photo-scrubs: #3c3f9a;
  }
  * { margin: 0; padding: 0; box-sizing: border-box; }
  html, body { width: 1200px; height: 1200px; overflow: hidden; }
  body { position: relative; background: var(--photo-light); }

  .ad { position: relative; width: 1200px; height: 1200px; overflow: hidden; }

  .surgeon-photo {
    position: absolute; inset: 0;
    background:
      radial-gradient(ellipse 420px 560px at 930px 850px, var(--photo-scrubs) 0%, rgba(60,63,154,0.85) 55%, rgba(60,63,154,0) 80%),
      linear-gradient(100deg, var(--photo-mid) 0%, var(--photo-light) 35%, #d9d6d8 60%, #b9b7c9 100%);
  }

  .panel {
    position: absolute; left: 90px; top: 24px; width: 613px; height: 1151px;
    border-radius: 32px;
    background: linear-gradient(180deg, var(--panel-top) 0%, rgba(34,146,150,0.9) 55%, var(--panel-bottom) 100%);
    color: var(--white);
    text-align: center;
  }

  .brand {
    position: absolute; left: 0; right: 0; top: 150px;
    display: flex; align-items: center; justify-content: center; gap: 14px;
    font-family: "Playfair Display", serif; font-weight: 400; color: var(--white);
  }
  .brand-dot { width: 22px; height: 22px; border-radius: 50%; background: var(--white); flex: none; }
  .brand-text { text-align: left; line-height: 1; }
  .brand-name { font-size: 32px; letter-spacing: 1px; text-transform: uppercase; }
  .brand-role { font-size: 11.5px; letter-spacing: 2.4px; text-transform: uppercase; margin-top: 4px; }

  .headline {
    position: absolute; left: 0; right: 0; top: 340px;
    font-family: "Playfair Display", serif; font-weight: 400;
    font-size: 86px; line-height: 97px; letter-spacing: -0.5px;
  }

  .subline {
    position: absolute; left: 0; right: 0; top: 650px;
    font-family: "Jost", sans-serif; font-weight: 300;
    font-size: 41px; line-height: 50px;
  }

  .cta {
    position: absolute; left: 182px; top: 840px; width: 250px; height: 56px;
    border-radius: 12px; background: var(--button);
    display: flex; align-items: center; justify-content: center;
    font-family: "Jost", sans-serif; font-weight: 300; font-size: 24px; color: var(--white);
  }
</style>
</head>
<body>
  <div class="ad">
    <div class="surgeon-photo" role="img" aria-label="Photo of a surgeon in blue scrubs and cap working in an operating theatre"></div>

    <section class="panel">
      <div class="brand">
        <span class="brand-dot"></span>
        <div class="brand-text">
          <div class="brand-name">Marcus Bellweather</div>
          <div class="brand-role">General, Upper GI &amp; Bariatric Surgeon</div>
        </div>
      </div>

      <h1 class="headline">Curious<br>about weight<br>loss surgery?</h1>

      <p class="subline">This 30 second quiz will<br>tell you which procedure<br>will suit you best</p>

      <div class="cta">Get Started!</div>
    </section>
  </div>
</body>
</html>
```